New Fernwick 4 Loop waste management business seeking web site

New project for business offering sustainable options within the waste industry.
Business called Fernwick 4 Loop
Targeting the consumer & industry professionals the web site needs to be able to accommodate both.
Needs to have a modern clean feel.
Logo being designed by another pro and will be completed early next week and will be submitted soon after to be incorporated into the web page
Links to another web page i like very much to take into consideration.

Target Market(s)

Industry professionals, consumers and producers of all waste, Food, constructruction, commercial, retail .. etc..

Industry/Entity Type

Waste Management

Coding

Coded - Design and coding required

Number of Pages Required

5+ page

Font styles to use
Serif
Script

Requirements
Must have
• Flexabilty, all pages as in examples
Nice to have
• Open to offers you guys and gals are the pro's

```html
<!DOCTYPE html>
<html lang="en">
<head>
<meta charset="utf-8">
<title>Fernwick 4 Loop</title>
<link href="https://fonts.googleapis.com/css2?family=Mulish:ital,wght@0,400;0,700;1,400&display=swap" rel="stylesheet">
<style>
:root{
  --white:#ffffff;
  --ink:#111111;
  --brand-green:#2a9d0e;
  --band:#2f9410;
  --band-text:#22800a;
  --footer:#256a10;
  --button:#23800c;
  --muted:#9a9a9a;
}
*{margin:0;padding:0;box-sizing:border-box}
html,body{width:682px;height:1200px;overflow:hidden;background:var(--white)}
body{position:relative;font-family:"Mulish",sans-serif;color:var(--ink)}
.abs{position:absolute}
.site-header{top:0;left:0;width:682px;height:28px;background:var(--white)}
.brand{left:61px;top:8px;font-size:10px;font-weight:400;color:var(--ink);letter-spacing:.2px}
.nav a{position:absolute;top:9px;font-size:8px;color:var(--ink);text-decoration:none}
.hero{top:28px;left:0;width:682px;height:189px;background:linear-gradient(135deg,#6fc24a 0%,#2fa44f 35%,#4fb8c8 55%,#3e7d2f 75%,#8bcb52 100%)}
.section-title{font-size:11px;font-weight:700}
.services-title{top:247px;left:0;width:682px;text-align:center}
.service{width:104px}
.service h3{font-size:8.5px;font-weight:700;color:var(--brand-green);height:26px}
.photo{width:104px;height:81px;border-radius:2px}
.service p{font-size:8.3px;line-height:13px;margin-top:14px;width:98px}
.ph-bags{background:linear-gradient(135deg,#3f5f9f,#2b6fd0 60%,#5b6a7a)}
.ph-food{background:linear-gradient(135deg,#c98a3a,#a23b22 45%,#7f8c3a)}
.ph-cans{background:linear-gradient(135deg,#c8a02a,#3a7a3a 45%,#a22a2a)}
.ph-card{background:linear-gradient(180deg,#6f9fd6 0%,#b09a7a 40%,#8a7356 100%)}
.ph-plant{background:linear-gradient(180deg,#3e7a46 0%,#a6a49a 55%,#6f6a60 100%)}
.work-band{top:473px;left:0;width:682px;height:237px;background:var(--band)}
.band-title{color:var(--white)}
.band-sub{font-size:10px;font-style:italic;color:var(--band-text)}
.work-copy{left:56px;top:558px;width:220px;font-size:7px;line-height:10.5px;color:var(--band-text)}
.circle{top:560px;width:104px;height:104px;border-radius:50%}
.blog-title{top:740px;left:56px}
.post{top:770px;width:80px}
.post .photo{width:78px;height:59px}
.post p{font-size:8.3px;line-height:12.8px;margin-top:13px;width:72px}
.post time{display:block;font-size:4px;color:var(--muted)}
.subscribe-band{top:968px;left:0;width:682px;height:184px;background:var(--band)}
.subscribe-copy{left:56px;top:1012px;width:140px;font-size:10px;line-height:16.5px;font-style:italic;color:var(--band-text)}
.field{left:211px;width:142px;height:21px;background:var(--white);border-radius:2px;font-size:7px;color:#b5b5b5;padding:5px 6px}
.signup{left:289px;top:1089px;width:64px;height:21px;background:var(--button);border-radius:2px;font-size:7px;color:#2f9a12;text-align:center;line-height:21px}
.site-footer{top:1152px;left:0;width:682px;height:48px;background:var(--footer)}
.footer-brand{left:56px;top:1163px;font-size:7px;font-weight:400;color:var(--white)}
.footer-links{font-size:5px;line-height:7.5px;color:#3aa017}
</style>
</head>
<body>
<header class="abs site-header">
  <div class="abs brand">Fernwick 4 Loop</div>
  <nav class="nav">
    <a style="left:179px" href="#">Work</a>
    <a style="left:216px" href="#">Insight</a>
    <a style="left:258px" href="#">Services</a>
    <a style="left:306px" href="#">About</a>
    <a style="left:347px" href="#">Contact Us</a>
  </nav>
</header>

<div class="abs hero" role="img" aria-label="Green illustration of a town with factories, houses, cars, a lake with solar panels and sunflowers"></div>

<h2 class="abs section-title services-title">Our Services</h2>
<div class="abs service" style="left:115px;top:276px"><h3>Commercial Waste</h3><div class="photo ph-bags" role="img" aria-label="Photo of blue rubbish bags"></div><p>Solutions for business</p></div>
<div class="abs service" style="left:230px;top:276px"><h3>Domestic Waste</h3><div class="photo ph-food" role="img" aria-label="Photo of vegetable food waste"></div><p>Having a clear out or doing up a property ? We can help</p></div>
<div class="abs service" style="left:346px;top:276px"><h3>Recycling</h3><div class="photo ph-cans" role="img" aria-label="Photo of crushed drink cans"></div><p>Our promise to you of 0% to landfill</p></div>
<div class="abs service" style="left:461px;top:276px"><h3>Packaging Compliance</h3><div class="photo ph-card" role="img" aria-label="Photo of baled cardboard"></div><p>Solutions for business</p></div>

<section class="abs work-band"></section>
<h2 class="abs section-title band-title" style="left:56px;top:502px">Our Work Process</h2>
<p class="abs band-sub" style="left:56px;top:518px">Let us show our work process</p>
<p class="abs work-copy">Lorem ipsum dolor sit amet, consectetur adipiscing elit, sed do eiusmod tempor incididunt ut labore et dolore magna aliqua. Ut enim ad minim veniam, quis nostrud exercitation ullamco laboris nisi ut aliquip ex ea commodo consequat. Duis aute irure dolor in reprehenderit in voluptate velit esse cillum dolore eu fugiat nulla pariatur. Excepteur sint occaecat cupidatat non proident, sunt in culpa qui officia deserunt mollit anim id est laborum.</p>
<div class="abs circle ph-plant" style="left:288px" role="img" aria-label="Photo of a recycling plant with bales"></div>
<div class="abs circle ph-plant" style="left:405px" role="img" aria-label="Photo of sorting machinery"></div>
<div class="abs circle ph-plant" style="left:520px" role="img" aria-label="Photo of a conveyor line over bales"></div>

<h2 class="abs section-title blog-title">From The Blog</h2>
<article class="abs post" style="left:56px"><div class="photo ph-bags" role="img" aria-label="Photo of blue rubbish bags"></div><p>Solutions for business</p><time>5th Dec 15</time></article>
<article class="abs post" style="left:146px"><div class="photo ph-food" role="img" aria-label="Photo of vegetable food waste"></div><p>Having a clear out or doing up a property ? We can help</p><time>5th Dec 15</time></article>
<article class="abs post" style="left:238px"><div class="photo ph-cans" role="img" aria-label="Photo of crushed drink cans"></div><p>Our promise to you of 0% to landfill</p><time>5th Dec 15</time></article>
<article class="abs post" style="left:327px"><div class="photo ph-card" role="img" aria-label="Photo of baled cardboard"></div><p>Solutions for business</p><time>5th Dec 15</time></article>
<article class="abs post" style="left:417px"><div class="photo ph-food" role="img" aria-label="Photo of vegetable food waste"></div><p>Having a clear out or doing up a property ? We can help</p><time>5th Dec 15</time></article>
<article class="abs post" style="left:509px"><div class="photo ph-cans" role="img" aria-label="Photo of crushed drink cans"></div><p>Our promise to you of 0% to landfill</p><time>5th Dec 15</time></article>

<section class="abs subscribe-band"></section>
<h2 class="abs section-title band-title" style="left:56px;top:995px;font-size:9.5px">Subscribe</h2>
<p class="abs subscribe-copy">Gain insight to our exclusive Mega Trends feature &amp; sign up to our quarterly reports</p>
<div class="abs field" style="top:997px">Name</div>
<div class="abs field" style="top:1027px">Email</div>
<div class="abs field" style="top:1058px">Website</div>
<div class="abs signup">Sign Up</div>

<footer class="abs site-footer"></footer>
<div class="abs footer-brand">Fernwick 4 Loop</div>
<div class="abs footer-links" style="left:134px;top:1161px">Work<br>Insight<br>Services</div>
<div class="abs footer-links" style="left:166px;top:1161px">About<br>Contact Us</div>
<div class="abs footer-links" style="left:134px;top:1187px">Privacy Policy &nbsp;|&nbsp; Terms of Use &nbsp;|&nbsp; Accessibility</div>
<div class="abs footer-links" style="left:565px;top:1187px">© 2015 Fernwick 4 Loop</div>
</body>
</html>
```